MRB - Stationery Design Project

We need stationery based on our logo.

Company info :
Cabinet Morvalle & Associés
Société à responsabilité limitée au capital de 200.000 FCFP
RCS Papeete 27586D - Numéro tahiti C36927
Centre d’affaires OPALE - Rue Gaston Berthelin
BP 51839 MAISON VERDA - 98713 Papeete
Tahiti - Polynésie française
Tél : +689 40 63 17 94
Fax : +689 40 72 39 58

Industry/Entity Type

It Company

Font styles to use
Sans Serif

```html
<!DOCTYPE html>
<html lang="fr">
<head>
<meta charset="utf-8">
<title>MRB – Cartes de visite</title>
<link rel="stylesheet" href="https://fonts.googleapis.com/css2?family=Questrial&display=swap">
<style>
  :root {
    --navy: #1b2a4a;
    --slate: #7e8f91;
    --ink: #6b6e72;
    --paper: #f7f8fa;
    --backdrop: #e8e8ed;
  }
  * { margin: 0; padding: 0; box-sizing: border-box; }
  html, body { width: 1200px; height: 934px; overflow: hidden; }
  body {
    background: var(--backdrop);
    font-family: "Questrial", "Century Gothic", sans-serif;
    position: relative;
  }
  .card {
    position: absolute;
    width: 520px;
    height: 320px;
    top: 307px;
    border-radius: 3px;
    overflow: hidden;
    box-shadow: 0 2px 6px rgba(0,0,0,0.12);
  }
  .card--back { left: 60px; background: var(--navy); }
  .card--front { left: 620px; background: var(--paper); }

  .brand {
    position: absolute;
    left: 0; right: 0;
    text-align: center;
  }
  .card--back .brand { top: 92px; color: #ffffff; }
  .card--front .brand { top: 40px; color: var(--navy); }
  .brand__mark {
    display: block;
    font-size: 78px;
    line-height: 1;
    letter-spacing: 2px;
  }
  .brand__name {
    display: block;
    font-size: 19px;
    margin-top: 4px;
  }
  .brand__tagline {
    display: block;
    font-size: 8px;
    letter-spacing: 0.4px;
    margin-top: 3px;
    color: var(--slate);
  }

  .holder {
    position: absolute;
    top: 176px;
    left: 0; right: 0;
    text-align: center;
  }
  .holder__name {
    color: var(--navy);
    font-size: 15px;
    font-weight: 700;
    letter-spacing: 0.5px;
  }
  .holder__role { color: var(--ink); font-size: 11px; margin-top: 2px; }

  .contact {
    position: absolute;
    right: 22px;
    bottom: 40px;
    text-align: right;
    color: var(--ink);
    font-size: 10.5px;
    line-height: 1.45;
  }
  .contact strong { color: var(--navy); }

  .band {
    position: absolute;
    bottom: 0;
    height: 14px;
  }
  .band--navy { left: 0; width: 60%; background: var(--navy); }
  .band--slate { right: 0; width: 39%; background: var(--slate); }
</style>
</head>
<body>
  <section class="card card--back" aria-label="Verso de la carte">
    <div class="brand">
      <span class="brand__mark">MRB</span>
      <span class="brand__name">Cabinet Morvalle &amp; Associés</span>
      <span class="brand__tagline">Expertise-comptable · Audit · Conseil</span>
    </div>
  </section>

  <section class="card card--front" aria-label="Recto de la carte">
    <div class="brand">
      <span class="brand__mark">MRB</span>
      <span class="brand__name">Cabinet Morvalle &amp; Associés</span>
      <span class="brand__tagline">Expertise-comptable · Audit · Conseil</span>
    </div>
    <div class="holder">
      <p class="holder__name">JULES TERRAND</p>
      <p class="holder__role">Managing Director</p>
    </div>
    <address class="contact" style="font-style:normal">
      Centre d’affaires OPALE - Rue Gaston Berthelin, BP 51839, MAISON VERDA - 98713 Papeete<br>
      Tahiti - Polynésie française · <strong>Tél:</strong> +689 40 63 17 94 · <strong>Fax:</strong> +689 40 72 39 58
    </address>
    <div class="band band--navy"></div>
    <div class="band band--slate"></div>
  </section>
</body>
</html>
```